TuneNest - Music Industry App needs a top quality wordpress homepage

We need a modern responsive wordpress homepage built. Our website will only feature one page with the goal to get people to sign up to our app. A word document has been uploaded outlining the page content/sections.

Once the homepage is finalised, I will also need 2 landing pages built as part of this competition. It will be very similar to the homepage with the same layout etc but just feature different images and content. The homepage is for anyone (artists and venues) to find out about us but the landing pages will be artist or venue specific.

The completed work must be delivered as an exportable file into wordpress and be designed properly so no more work is needed to begin utilising as the actual website. The images used must be setup correctly for speed and quality also.

Target Market(s)

Venues and Artists.

Coding

Coded - Design and coding required

Requirements
Must have
• UPDATE: High Res Logo files attached
• Must be a modern looking website and be responsive. Must look good across all devices from desktop, to mobile and tablet. Needs to be very high quality.
• Please see the attached logo - I am waiting for the final high quality version and will reupload when complete but this will be enough to get you started for now. The website must have a dark base colour and have red/white elements to match the logo. The red colour used MUST match the red colour used in the logo.
• Please have a go at creating it how you think is best and provide feedback from there. I am leaving it very open to the designers so I can get the best website possible and lots of different ideas etc.

```html
<!DOCTYPE html>
<html lang="en">
<head>
<meta charset="utf-8">
<title>TuneNest – Live Music Booking</title>
<link href="https://fonts.googleapis.com/css2?family=Poppins:wght@300;400;500;600;700;800&display=swap" rel="stylesheet">
<style>
:root{
  --navy:#0d1a30;
  --card:#15233d;
  --red:#e3111b;
  --white:#ffffff;
  --muted:#8a94a8;
  --ghost:rgba(255,255,255,0.03);
  --line:rgba(255,255,255,0.35);
}
*{box-sizing:border-box;margin:0;padding:0}
html,body{width:1200px;height:4029px;overflow:hidden}
body{background:var(--navy);color:var(--white);font-family:'Poppins',sans-serif;position:relative}
.abs{position:absolute}
.hero{position:absolute;left:0;top:0;width:1200px;height:700px;background:linear-gradient(180deg,#3a3f48 0%,#2a3140 40%,#16233a 80%,var(--navy) 100%)}
.hero-photo{position:absolute;inset:0;background:radial-gradient(ellipse at 55% 20%,rgba(200,200,200,.35),transparent 60%)}
.brand{position:absolute;left:84px;top:40px;display:flex;align-items:center;gap:10px;font-weight:600;font-size:26px;color:var(--white)}
.brand-dot{width:26px;height:26px;border-radius:50%;background:var(--red)}
.nav{position:absolute;top:43px;left:345px;display:flex;font-size:13px;letter-spacing:1.6px;color:#e6e8ee}
.nav span{margin-right:56px}
.nav-cta{position:absolute;left:1002px;top:31px;width:110px;height:43px;border-radius:22px;background:var(--red);font-weight:600;font-size:13px;display:flex;align-items:center;justify-content:center}
.hero-title{position:absolute;top:247px;width:1200px;text-align:center;font-weight:800;font-size:58px;letter-spacing:4px}
.hero-sub{position:absolute;top:334px;width:1200px;text-align:center;font-size:17px;color:#e6e8ee}
.signup{position:absolute;height:62px;border-radius:31px;background:var(--white);display:flex;align-items:center}
.signup .field{flex:1;padding-left:28px;font-size:13px;color:#6b7280;letter-spacing:1px}
.signup .btn{height:100%;border-radius:31px;background:var(--red);color:var(--white);font-weight:600;display:flex;align-items:center;justify-content:center;border:2px solid var(--white)}
.ghost{position:absolute;width:1200px;text-align:center;font-weight:800;font-size:118px;color:var(--ghost);white-space:nowrap}
.heading{position:absolute;width:1200px;text-align:center;font-weight:700;font-size:32px}
.step-icon{position:absolute;width:80px;height:80px}
.step-text{position:absolute;width:160px;text-align:center;font-size:13px;line-height:16px;color:var(--muted)}
.photo{position:absolute;top:1106px;height:421px}
.card{position:absolute;top:1767px;width:247px;height:283px;background:var(--card);text-align:center}
.card-icon{width:120px;height:120px;border-radius:50%;background:var(--navy);margin:20px auto 0;display:flex;align-items:center;justify-content:center}
.card h3{font-size:15px;font-weight:600;margin-top:30px;text-transform:uppercase}
.card p{font-size:13px;line-height:16px;color:var(--muted);margin:14px auto 0;width:205px}
.va-bg{position:absolute;left:0;top:2090px;width:1200px;height:820px;background:radial-gradient(ellipse at 50% 70%,rgba(60,70,110,.35),transparent 65%)}
.col-title{position:absolute;top:2255px;font-size:34px;font-weight:600}
.list{position:absolute;top:2320px;width:420px;list-style:none}
.list li{position:relative;padding-left:30px;font-size:14px;line-height:21px;margin-bottom:14px}
.list li::before{content:"";position:absolute;left:2px;top:3px;border-left:13px solid var(--red);border-top:7px solid transparent;border-bottom:7px solid transparent}
.promo{position:absolute;top:2585px;width:488px;height:198px;border:2px solid var(--white);padding:16px 18px}
.promo p{font-size:14px;line-height:21px;color:#8d97ab}
.promo .red{color:var(--red)}
.about-text{position:absolute;left:91px;top:3130px;width:545px;font-size:14px;line-height:25px}
.btn-red{position:absolute;background:var(--red);border-radius:26px;display:flex;align-items:center;justify-content:center;font-size:12px;font-weight:500}
.contact{position:absolute;left:0;top:3443px;width:1200px;height:586px;background:linear-gradient(180deg,#1c2a44,#111d33)}
.label{position:absolute;font-size:13px;text-transform:uppercase}
.small{position:absolute;font-size:12px;line-height:30px}
.form-field{position:absolute;left:700px;width:388px;border-bottom:1px solid var(--line);font-size:14px}
.social{position:absolute;top:3873px;display:flex;gap:30px;left:100px}
.social span{width:18px;height:18px;background:var(--white);display:block}
.footer-line{position:absolute;left:0;top:3975px;width:1200px;height:1px;background:var(--line)}
.copy{position:absolute;top:3991px;width:1200px;text-align:center;font-size:13px;letter-spacing:1px}
</style>
</head>
<body>

<header class="hero">
  <div class="hero-photo" role="img" aria-label="Concert crowd with raised hands under stage lights"></div>
  <div class="brand"><span class="brand-dot"></span>TuneNest</div>
  <nav class="nav"><span>ARTISTS</span><span>PRODUCERS</span><span>LIVE STAGE</span><span>SYNC</span><span>ABOUT US</span></nav>
  <div class="nav-cta">Sign Up</div>
  <h1 class="hero-title">ZIPCAB FOR LIVE MUSIC</h1>
  <p class="hero-sub">"TuneNest connects venues with artists to make booking gigs simple"</p>
  <div class="signup" style="left:313px;top:402px;width:566px">
    <div class="field">Email Address</div>
    <div class="btn" style="width:157px;font-size:17px">Sign Up</div>
  </div>
</header>

<div class="ghost" style="top:730px">How We work</div>
<h2 class="heading" style="top:787px">How TuneNest Works</h2>

<svg class="abs" style="left:0;top:895px" width="1200" height="90" fill="none" stroke="#e3111b" stroke-width="2" stroke-dasharray="3 4">
  <path d="M210 60 Q255 100 300 65"/><path d="M410 35 Q460 -5 510 35"/>
  <path d="M630 60 Q680 100 735 60"/><path d="M860 35 Q910 -5 965 35"/>
</svg>

<svg class="step-icon" style="left:112px;top:898px" viewBox="0 0 80 80" fill="none" stroke="#fff" stroke-width="2.5"><rect x="24" y="4" width="40" height="66"/><rect x="6" y="28" width="18" height="42"/><path d="M32 14h6M44 14h6M32 26h6M44 26h6M32 38h6M44 38h6M32 50h6M44 50h6M0 70h76"/><circle cx="20" cy="62" r="10" fill="#0d1a30"/><path d="M15 62l4 4 7-8"/></svg>
<svg class="step-icon" style="left:321px;top:898px" viewBox="0 0 80 80" fill="none" stroke="#fff" stroke-width="2.5"><circle cx="40" cy="46" r="28"/><circle cx="40" cy="46" r="21"/><path d="M34 6h12M40 6v12"/><text x="40" y="55" text-anchor="middle" font-size="24" fill="#fff" stroke="none" font-family="Poppins, sans-serif">$</text></svg>
<svg class="step-icon" style="left:520px;top:898px" viewBox="0 0 80 80" fill="none" stroke="#fff" stroke-width="2.5"><path d="M32 6h16l-4 10h-8z"/><path d="M36 16c-14 10-16 34 4 36 20-2 18-26 4-36"/><path d="M4 60l14-8h20l10 6h22M4 76l16-8 26 4 28-14"/><text x="40" y="44" text-anchor="middle" font-size="20" fill="#fff" stroke="none" font-family="Poppins, sans-serif">$</text></svg>
<svg class="step-icon" style="left:760px;top:898px" viewBox="0 0 80 80" fill="none" stroke="#fff" stroke-width="2.5"><rect x="4" y="4" width="72" height="52"/><rect x="12" y="12" width="56" height="36"/><path d="M36 24l10 6-10 6z M32 56v12h16V56 M22 74h36"/></svg>
<svg class="step-icon" style="left:976px;top:898px" viewBox="0 0 80 80" fill="none" stroke="#fff" stroke-width="2.5"><path d="M28 4h26a8 8 0 0 1 8 8v12a8 8 0 0 1-8 8H40l-8 6v-6h-4a8 8 0 0 1-8-8V12a8 8 0 0 1 8-8z"/><circle cx="40" cy="48" r="7"/><circle cx="18" cy="52" r="7"/><circle cx="62" cy="52" r="7"/><path d="M4 76a14 14 0 0 1 28 0M26 70a14 14 0 0 1 28 0M48 76a14 14 0 0 1 28 0"/></svg>

<p class="step-text" style="left:72px;top:1010px">Artists and venues sign up for free and create a profile.</p>
<p class="step-text" style="left:281px;top:1010px">Venues search for an artist for their upcoming gigs.</p>
<p class="step-text" style="left:497px;top:1010px">Venues request a quote and communicate with the artist direct.</p>
<p class="step-text" style="left:716px;top:1012px">The gig is booked in once payment is provided by the venue.</p>
<p class="step-text" style="left:936px;top:1012px">Upon completion the money is paid to the artist within 48 hours / less.</p>

<div class="photo" style="left:85px;width:317px;background:linear-gradient(160deg,#4a2c1c,#1d1410 70%)" role="img" aria-label="Singer playing an acoustic guitar beside a guitarist in a warm lit bar"></div>
<div class="photo" style="left:429px;width:325px;background:linear-gradient(180deg,#3a5f9a,#1b2a48 40%,#2a241e 100%)" role="img" aria-label="Large festival crowd facing a brightly lit stage"></div>
<div class="photo" style="left:784px;width:327px;background:linear-gradient(160deg,#5a3a22,#2a1c14 70%)" role="img" aria-label="Guitarist and singer performing together on a small stage"></div>

<div class="ghost" style="top:1590px">Why TuneNest?</div>
<h2 class="heading" style="top:1649px">Why TuneNest ?</h2>

<div class="card" style="left:85px">
  <div class="card-icon"><svg width="64" height="64" viewBox="0 0 80 80" fill="none" stroke="#fff" stroke-width="2.5"><rect x="24" y="4" width="40" height="66"/><rect x="6" y="28" width="18" height="42"/><path d="M32 14h6M44 14h6M32 26h6M44 26h6M32 38h6M44 38h6M0 70h76"/><circle cx="20" cy="62" r="10" fill="#0d1a30"/><path d="M15 62l4 4 7-8"/></svg></div>
  <h3>Easy Booking</h3><p>TuneNest makes gig booking easy for both the venue and artist.</p>
</div>
<div class="card" style="left:344px">
  <div class="card-icon"><svg width="64" height="64" viewBox="0 0 80 80" fill="none" stroke="#fff" stroke-width="2.5"><circle cx="22" cy="14" r="8"/><path d="M10 74V40a12 12 0 0 1 24 0v34M34 40l20-14"/><rect x="40" y="6" width="36" height="26"/><circle cx="56" cy="50" r="7"/><path d="M44 74a12 12 0 0 1 24 0"/></svg></div>
  <h3>Join Community</h3><p>Join the TuneNest community which is full of amazing artists and venues.</p>
</div>
<div class="card" style="left:603px">
  <div class="card-icon"><svg width="64" height="64" viewBox="0 0 80 80" fill="none" stroke="#fff" stroke-width="2.5"><path d="M40 4l30 10v24c0 18-14 32-30 38C24 70 10 56 10 38V14z"/><path d="M40 12l22 8v18c0 13-10 24-22 29-12-5-22-16-22-29V20z"/><circle cx="40" cy="40" r="10"/><path d="M35 40l4 4 6-7"/></svg></div>
  <h3>Protected Resolutions</h3><p>Everyone is protected with our complimentary dispute resolutions.</p>
</div>
<div class="card" style="left:861px">
  <div class="card-icon"><svg width="64" height="64" viewBox="0 0 80 80" fill="none" stroke="#fff" stroke-width="2.5"><path d="M24 10h52v36H54l-8 8v-8H24z"/><path d="M34 22h32M34 30h32M34 38h20"/><path d="M18 28H4v30h8v10l10-10h22v-8"/><path d="M10 40h6M20 40h6"/></svg></div>
  <h3>Best Possible Rates</h3><p>Get the best rate possible with TuneNest only receiving 5% of the artists fee</p>
</div>

<div class="va-bg" role="img" aria-label="Faint concert crowd with raised hands behind the section"></div>
<div class="ghost" style="top:2090px">Venue &amp; Artist</div>
<h2 class="heading" style="top:2166px">Venue &amp; Artists</h2>

<h3 class="col-title" style="left:88px">Venue</h3>
<ul class="list" style="left:88px">
  <li>TuneNest is a 100% FREE service for all venues - you pay us nothing!</li>
  <li>Get instant access to hundreds of artists around your local community</li>
  <li>All genres to suit any venue from a pub to a wedding or even a nightclub</li>
  <li>Simple booking process with a money back guarantee</li>
  <li>Communicate directly with the artist and negotiate</li>
</ul>
<h3 class="col-title" style="left:601px">Artists</h3>
<ul class="list" style="left:601px">
  <li>Sign up to TuneNest for FREE and get yourself in front of venues</li>
  <li>Only pay us if you get a gig - we only get 5% of the fee you charge the venue</li>
  <li>All genres and artists welcome - as long as you're experienced and professional</li>
  <li>Get paid within 48 hours or less after the gig guaranteed!</li>
  <li>Negotiate your price and don't pay huge agent fees to ensure you earn top dollar</li>
</ul>

<div class="promo" style="left:97px">
  <p>TuneNest is not yet ready to host gigs as we're currently working on building our artists. We are launching for venues in Q4 2019. Pre-register now to keep informed and be one of the first people to use our platform.</p>
  <div class="signup" style="left:18px;top:128px;width:410px;height:46px">
    <div class="field" style="padding-left:22px;font-size:12px">Email Address</div>
    <div class="btn" style="width:122px;font-size:13px">Sign Up</div>
  </div>
</div>
<div class="promo" style="left:613px">
  <p><span class="red">Sign up</span> and create your TuneNest profile now.</p>
  <p style="margin-top:19px">It is a long established fact that a reader will be distracted by the readable content of a page .</p>
  <div class="signup" style="left:16px;top:128px;width:410px;height:46px">
    <div class="field" style="padding-left:18px;font-size:12px">Email Address</div>
    <div class="btn" style="width:122px;font-size:13px">Sign Up</div>
  </div>
</div>

<div class="ghost" style="top:2985px">About TuneNest</div>
<h2 class="heading" style="top:3063px">About TuneNest</h2>
<p class="about-text">It is a long established fact that a reader will be distracted by the readable content of a page when looking at its layout. The point of using Lorem Ipsum is that it has a more-or-less normal distribution of letters, as opposed to using 'Content here, content here', making it look like readable English. Many desktop publishing packages</p>
<div class="btn-red" style="left:92px;top:3323px;width:160px;height:51px">Know More</div>
<div class="abs" style="left:657px;top:3150px;width:454px;height:243px;background:linear-gradient(135deg,#4a4036,#1f1c1a 60%,#3a2f28)" role="img" aria-label="Three founders posing together in front of bookshelves"></div>

<section class="contact" role="img" aria-label="Dark concert crowd silhouettes behind the contact section"></section>
<div class="ghost" style="top:3475px">Contact Us</div>
<h2 class="heading" style="top:3545px">Contact Us</h2>

<div class="label" style="left:94px;top:3641px">Address</div>
<div class="small" style="left:96px;top:3665px">88 Harbor Lane,<br>Suite 12<br>TuneNest, Music 40210<br>(000) 555-0142<br>Map / Directions</div>
<div class="label" style="left:371px;top:3638px">Quick links</div>
<div class="small" style="left:376px;top:3663px;line-height:26px">Artists<br>Producers<br>Live Stage<br>Sync<br>About</div>
<div class="social"><span></span><span></span><span></span><span></span></div>

<div class="form-field" style="top:3600px;height:44px;padding-left:14px">User name</div>
<div class="form-field" style="top:3671px;height:44px;padding-left:14px">Email address</div>
<div class="form-field" style="top:3761px;height:98px;padding-left:14px">Your message</div>
<div class="btn-red" style="left:700px;top:3894px;width:159px;height:48px">Submit</div>

<div class="footer-line"></div>
<p class="copy">© 2019 TuneNest &amp; Company. All rights reserved. Disclaimer</p>

</body>
</html>
```